Tarvon Letterhead

Looking for a design template for our company’s official letterheads & business cards.It has to be mainly white and include our company logo, website, social media handle, address, phone number. Visit our website to have an idea of our brand identity and colours. Please use the same font that we are using in our website.
Target Market(s)
Lubricants & Greases, Industrial markets, Automotive
Font styles to use
Other font styles liked:
- Saira Extra-Condensed
Colors
ffffff
000000
fbee3f
Requirements
Must have
- It must be consistent with our brand identity. It must use the same exact yellow (Pantone color: 102C) and black (Pantone color: K100) as our brand colors.
- Must also use our font attached (Saira.zip). It's called Saira Extra-Condensed.
- We intend to use the TARVON logo and not the small mini-TV logo.
- On the design we must include ALL of the following:
- E-mail: info@tarvonfluids.example
- @TarvonFluids
- www.tarvonfluids.example
- Address: P.O. Boc 4827, Qurain 73504, Kuwait
- Phone: (+965) 24718593
- Kuwait Morel Oils logo (attached). The logo attached is in Blue/Red but you can select one solid color for all of it such as BLACK or YELLOW depending on what background color you'll select.
Nice to have
- Like it to be as professional and as modern as possible. It has look clean, slick and classy.
Should not have
- Too many different colors.

```html
<!DOCTYPE html>
<html lang="en">
<head>
<meta charset="utf-8">
<title>Tarvon Stationery</title>
<link href="https://fonts.googleapis.com/css2?family=Saira+Extra+Condensed:wght@400;500;600;700&family=Questrial&display=swap" rel="stylesheet">
<style>
  :root {
    --yellow: #fbee3f;
    --brand-yellow: #f2e100;
    --black: #1a1a1a;
    --ink: #231f20;
    --paper: #ffffff;
    --paper-soft: #f7f7f7;
    --stage: #e3e3e3;
    --rule: #555555;
    --sig-tint: #dfe7f3;
    --condensed: "Saira Extra Condensed", "Arial Narrow", sans-serif;
  }
  * { box-sizing: border-box; margin: 0; padding: 0; }
  html, body { width: 1200px; height: 966px; overflow: hidden; }
  body {
    position: relative;
    background: radial-gradient(ellipse at 55% 45%, #ececec 0%, var(--stage) 70%, #d9d9d9 100%);
    font-family: "Questrial", sans-serif;
    color: var(--ink);
  }
  .sheet, .card { position: absolute; box-shadow: 0 2px 6px rgba(0,0,0,.18); overflow: hidden; }

  /* Brand wordmark */
  .wordmark { display: flex; align-items: center; gap: 6px; }
  .wordmark__square { width: 12px; height: 12px; background: var(--brand-yellow); flex: none; }
  .wordmark__name {
    font-family: var(--condensed); font-weight: 700;
    color: var(--black); letter-spacing: 1px; line-height: 1; white-space: nowrap;
  }

  /* Letterhead */
  .letterhead { left: 530px; top: 70px; width: 580px; height: 814px; background: linear-gradient(180deg, var(--paper) 0%, var(--paper-soft) 100%); }
  .letterhead .wordmark { position: absolute; left: 53px; top: 70px; }
  .letterhead .wordmark__square { width: 16px; height: 16px; }
  .letterhead .wordmark__name { font-size: 48px; }

  .lh-header-info {
    position: absolute; right: 46px; top: 76px;
    display: flex; align-items: stretch; gap: 14px;
  }
  .lh-address {
    font-style: normal; text-align: right; white-space: nowrap;
    font-family: var(--condensed); font-size: 10px; line-height: 12px; color: var(--ink);
  }
  .lh-divider { width: 1px; background: var(--rule); }
  .contact-list { list-style: none; font-family: var(--condensed); color: var(--ink); white-space: nowrap; }
  .contact-list li { display: flex; align-items: center; gap: 5px; }
  .contact-list svg { width: 8px; height: 8px; flex: none; fill: var(--brand-yellow); }
  .lh-contacts { font-size: 10px; line-height: 12px; }

  .letter { position: absolute; left: 51px; top: 222px; width: 483px; }
  .letter .letter__salutation { font-size: 15px; line-height: 18px; color: #444; margin-bottom: 22px; text-align: left; }
  .letter p { font-size: 8px; line-height: 10.5px; color: #555; text-align: justify; margin-bottom: 9.5px; }
  .letter .letter__closing { font-size: 8px; color: #555; margin-top: 22px; text-align: left; }
  .signature { position: absolute; left: 47px; top: 566px; width: 105px; height: 46px; background: var(--sig-tint); border-radius: 4px; }

  .partner { position: absolute; display: flex; align-items: center; gap: 6px; }
  .partner__circle { width: 20px; height: 20px; border-radius: 50%; flex: none; }
  .partner__name { font-family: var(--condensed); font-weight: 600; font-size: 10px; letter-spacing: .3px; white-space: nowrap; }
  .letterhead .partner { left: 53px; top: 752px; }
  .letterhead .partner__circle { background: var(--ink); }
  .letterhead .partner__name { color: var(--ink); }

  .footer-band { position: absolute; left: 0; bottom: 0; }
  .web {
    position: absolute; font-family: var(--condensed); font-weight: 700;
    color: var(--black); letter-spacing: 0; white-space: nowrap; line-height: 1;
  }
  .letterhead .web { right: 22px; bottom: 8px; font-size: 10px; }

  /* Business card front */
  .card { width: 412px; height: 236px; }
  .card--front { left: 81px; top: 380px; background: linear-gradient(180deg, var(--paper) 0%, var(--paper-soft) 100%); }
  .card--front .wordmark { position: absolute; right: 26px; top: 34px; }
  .card--front .wordmark__square { width: 18px; height: 18px; }
  .card--front .wordmark__name { font-size: 52px; }
  .holder { position: absolute; left: 18px; top: 112px; font-family: var(--condensed); white-space: nowrap; }
  .holder__name { font-size: 16px; font-weight: 700; color: #e4d400; letter-spacing: .5px; line-height: 18px; }
  .holder__role { font-size: 10px; font-weight: 600; color: var(--ink); letter-spacing: .4px; line-height: 13px; }
  .card__rule { position: absolute; left: 18px; top: 151px; width: 369px; height: 1px; background: var(--rule); }
  .card-contacts { position: absolute; left: 20px; top: 162px; font-size: 10px; line-height: 14px; }
  .card-address {
    position: absolute; right: 25px; top: 162px; text-align: right; font-style: normal; white-space: nowrap;
    font-family: var(--condensed); font-size: 10px; line-height: 14px; color: var(--ink);
  }
  .card--front .web { right: 14px; bottom: 7px; font-size: 10px; }

  /* Business card back */
  .card--back { left: 81px; top: 647px; background: var(--black); }
  .card--back .wordmark { position: absolute; left: 50%; top: 80px; transform: translateX(-50%); }
  .card--back .wordmark__square { width: 20px; height: 20px; }
  .card--back .wordmark__name { font-size: 60px; color: var(--brand-yellow); }
  .card--back .partner { right: 24px; bottom: 22px; }
  .card--back .partner__circle { width: 18px; height: 18px; background: var(--brand-yellow); }
  .card--back .partner__name { color: var(--brand-yellow); font-size: 9px; }
</style>
</head>
<body>

  <section class="sheet letterhead" aria-label="Letterhead">
    <div class="wordmark">
      <span class="wordmark__name">TARVON</span>
      <span class="wordmark__square"></span>
    </div>

    <div class="lh-header-info">
      <address class="lh-address">P.O. Boc 4827<br>Qurain 73504<br>Kuwait</address>
      <div class="lh-divider"></div>
      <ul class="contact-list lh-contacts">
        <li><svg viewBox="0 0 10 10"><path d="M2 0.5 L4 2.5 L3 4 Q4.5 6 6 7 L7.5 6 L9.5 8 L8 9.5 Q3 9 0.5 2 Z"/></svg>(+965) 24718593</li>
        <li><svg viewBox="0 0 10 10"><rect x="0" y="2" width="10" height="6.5"/></svg>info@tarvonfluids.example</li>
        <li><svg viewBox="0 0 10 10"><circle cx="5" cy="5" r="4"/></svg>@TarvonFluids</li>
      </ul>
    </div>

    <article class="letter">
      <p class="letter__salutation">Dear Mr. Nassar,</p>
      <p>Lorem ipsum dolor sit amet, consectetur adipiscing elit. Donec orci purus, luctus vitae dignissim eu, iaculis sed purus. Vivamus faucibus, ipsum nec aliquet viverra, leo mauris condimentum ligula, sit amet sagittis enim ligula quis arcu. Nam egestas tortor id nisi porttitor mattis. In tortor ante, ultricies in suscipit a, tempus non massa. Vivamus et auctor mi. Fusce vel massa nulla. Phasellus nec eros mauris, et scelerisque orci.</p>
      <p>Donec malesuada orci vitae nulla accumsan porta a id massa. Quisque accumsan iaculis magna sit amet fringilla. Maecenas consequat, magna eget tincidunt semper, odio nibh rutrum mi, id feugiat ante nisi eu risus. Vestibulum nunc orci, rhoncus a placerat in, ultricies in mi. Cras mattis varius eros, vel fringilla nisi suscipit eget. Quisque scelerisque sagittis nulla at porttitor.</p>
      <p>Sed id augue vitae urna euismod commodo aliquet a quam. Pellentesque arcu velit, cursus et malesuada ut, consequat et diam. Nullam erat sem, rhoncus id ullamcorper vitae, rhoncus et arcu. In ultricies ultricies nulla, ut rutrum nisi iaculis at. Donec eu magna a metus ornare faucibus. Fusce aliquet faucibus ultricies. Morbi semper, est id tincidunt gravida, sem arcu adipiscing lacus, ac bibendum nulla leo eu purus. Quisque nec diam sed risus consectetur a ccumsan quis quis nibh. Vestibulum id purus lorem.</p>
      <p>It is a long established fact that a reader will be distracted by the readable content of a page when looking at its layout. The point of using Lorem Ipsum is that it has a more-or-less normal distribution of letters, as opposed to using 'Content here, content here', making it look like readable English. Many desktop publishing packages</p>
      <p class="letter__closing">Sincerely,</p>
    </article>
    <div class="signature" role="img" aria-label="Handwritten signature of Karim Nassar in blue ink"></div>

    <div class="partner">
      <span class="partner__circle"></span>
      <span class="partner__name">KUWAIT MOREL OILS CO.</span>
    </div>

    <svg class="footer-band" width="580" height="26" viewBox="0 0 580 26">
      <rect x="0" y="8" width="400" height="6" fill="#1a1a1a"/>
      <rect x="0" y="15" width="400" height="5" fill="#f2e100"/>
      <polygon points="405,0 580,0 580,26 380,26" fill="#f2e100"/>
    </svg>
    <span class="web">WWW.TARVONFLUIDS.EXAMPLE</span>
  </section>

  <section class="card card--front" aria-label="Business card front">
    <div class="wordmark">
      <span class="wordmark__name">TARVON</span>
      <span class="wordmark__square"></span>
    </div>
    <div class="holder">
      <div class="holder__name">KARIM NASSAR</div>
      <div class="holder__role">CEO/FOUNDER</div>
    </div>
    <div class="card__rule"></div>
    <ul class="contact-list card-contacts">
      <li><svg viewBox="0 0 10 10"><path d="M2 0.5 L4 2.5 L3 4 Q4.5 6 6 7 L7.5 6 L9.5 8 L8 9.5 Q3 9 0.5 2 Z"/></svg>(+965) 24718593</li>
      <li><svg viewBox="0 0 10 10"><rect x="0" y="2" width="10" height="6.5"/></svg>info@tarvonfluids.example</li>
      <li><svg viewBox="0 0 10 10"><circle cx="5" cy="5" r="4"/></svg>@TarvonFluids</li>
    </ul>
    <address class="card-address">P.O. Boc 4827<br>Qurain 73504<br>Kuwait</address>
    <svg class="footer-band" width="412" height="24" viewBox="0 0 412 24">
      <rect x="0" y="8" width="225" height="5" fill="#1a1a1a"/>
      <rect x="0" y="14" width="225" height="5" fill="#f2e100"/>
      <polygon points="240,0 412,0 412,24 218,24" fill="#f2e100"/>
    </svg>
    <span class="web">WWW.TARVONFLUIDS.EXAMPLE</span>
  </section>

  <section class="card card--back" aria-label="Business card back">
    <div class="wordmark">
      <span class="wordmark__name">TARVON</span>
      <span class="wordmark__square"></span>
    </div>
    <div class="partner">
      <span class="partner__circle"></span>
      <span class="partner__name">KUWAIT MOREL OILS CO.</span>
    </div>
  </section>

</body>
</html>
```